Website for online Real Estate School

I need to have three drop boxes which are really the main item on our web site. These tabs will need to be front and center “call to action”. Our sole goal on our site is to sell real estate courses which will be connected to these drop boxes. So please make this “call to action” section “clean” and the main emphasis on the page. We will fill in the items in the drop box so please ensure we have that ability.

 Get your license
 Post-Licensing
 Continuing Education

You could use the statement; “The Path to Your Future”

I’d like the design to be one where you keep scrolling down instead of having 5 or 6 tabs up top with different pages.

As you scan down I’d like to include the graphics and text as shown on one of the attachments. I copied this from another site so I’d ask you provide another logo. I already amended the text

People enter the real estate field with diverse educational backgrounds and overall goals. Some enter to only work part time to supplement their current income, and others full time. One person may enter the commercial market space and another residential. There is a wide range of directions you can take and the sky is truly the limit. Whichever path you take, your chances of success are directly related to your level of preparation and commitment. This is one career that really rewards self-motivated individuals.

 Careers - Career fields include residential and commercial real estate agents, brokers, mortgage brokers, property managers and independent investors. Many of these careers are held by independent people who have a strong entrepreneurial spirit. As you enter the real estate business in general its not unlikely you will be in it for life in one way or another. In our opinion it truly is the best path to wealth.
 Salary - According to the Norland Office of Trade Figures, real estate brokers earned a median annual wage of $56,860 and the highest 10 percent earned more than $166,940. An agent’s income is only limited to how much work you want to put into your business. We highly suggest you consider a few of our partners offers below as they can truly help you work smarter, not harder.
 Degrees - A real estate license will provide all you will need to enter the real estate business. Each state has requirements that you complete “Continuing Education” every other year. There are several other courses that will provide you with certifications which demonstrate your sophistication therefore we recommend you continue your pursuit of education and we certainly hope you do so with us.

We highly recommend you consider a few of out strategic partners as their services are a tremendous advantage to real estate professionals.

Here we will have 6-8 banners from companies that we will be affiliates with.

At this point I’m not interested in providing an address nor phone number for contact.

Our web site domain is; www.MeridelPropertyAcademy.com

I have a number of graphics that I will upload the .ai file. Feel free to improve as you see fit.

I included a few copies of our competition. PLEASE, do some basic research.... in short, we are a national school that sells real estate licensing education for your initial license and also continuing education. We sooooooo want to be better than our competitors. Please help us achieve this. zintro real estate license and real estate continuing education and look at competitors... Please. That way you truly know what we need to beat.

This is my 40th ish project on craft hive and appreciate everyone's work which is why I always come back.

We will be EXTREMELY RESPONSIVE AND LOG ON 5-10X A DAY TO COMMENT ON DESIGNS. PLEASE ONLY MESSAGE US ON THE DESIGN ITSELF VS VIA THE MAIL SYSTEM AS ITS EASIER FOR US. THANKS!!!

Reason: We have extended this project for 5 days as we think 2 days was a bit ambitious. We look forward to your designs

18-40 year old consumers. Aspiring and existing real estate agents and brokers

Real Estate

Coded - Design and coding required

1 page

• your choice

• clean site... please review the competition by searching on zintro; real estate continuing education and real estate license
• just clean site. nice and simple and be sure to have the call to action sections as the emphasis

```html
<!DOCTYPE html>
<html lang="en">
<head>
<meta charset="utf-8">
<title>Meridel Property Academy</title>
<link href="https://fonts.googleapis.com/css2?family=Open+Sans:wght@400;600&family=Roboto+Slab:wght@400&family=Ubuntu:wght@400;500;700&display=swap" rel="stylesheet">
<style>
:root{
  --brand-blue:#3f8bc9;
  --brand-blue-deep:#2f74b0;
  --charcoal:#434145;
  --charcoal-dark:#2c2a2e;
  --ink:#222226;
  --white:#ffffff;
  --navy:#0b1824;
  --muted:#cfd8e2;
}
*{box-sizing:border-box;margin:0;padding:0}
html,body{width:671px;height:1200px;overflow:hidden;background:var(--white)}
body{position:relative;font-family:"Open Sans",Arial,sans-serif;color:var(--ink)}
.abs{position:absolute}

/* Header */
.top-rule{left:0;top:0;width:671px;height:3px;background:var(--charcoal)}
.site-header{left:0;top:3px;width:671px;height:69px;background:var(--brand-blue)}
.brand{left:56px;top:0;width:140px;height:69px;display:flex;flex-direction:column;align-items:center;justify-content:center;gap:6px}
.brand-mark{width:22px;height:22px;border-radius:50%;background:var(--white)}
.brand-name{font-family:"Ubuntu",sans-serif;font-weight:700;font-size:8.6px;color:var(--white);letter-spacing:.2px;white-space:nowrap}
.main-nav{top:0;height:69px;display:flex;align-items:center}
.main-nav a{position:absolute;top:30px;font-family:"Open Sans",sans-serif;font-size:8.2px;color:var(--white);text-decoration:none;white-space:nowrap;letter-spacing:.2px}

/* Hero */
.hero{left:0;top:72px;width:671px;height:310px}
.hero-photo{left:0;top:0;width:671px;height:310px;background:radial-gradient(ellipse at 45% 45%,#1f4f78 0%,#0f2a42 38%,#081521 70%),#081521}
.hero-wave{left:0;top:275px;width:671px;height:36px}
.hero-title{left:0;top:198px;width:671px;text-align:center;font-family:"Roboto Slab",serif;font-size:27px;color:var(--white);text-shadow:0 2px 4px rgba(0,0,0,.6)}
.hero-button{left:298px;top:246px;width:71px;height:26px;background:var(--brand-blue);color:var(--white);font-size:8.8px;display:flex;align-items:center;justify-content:center}
.slider-dots{left:318px;top:353px;display:flex;gap:4px}
.slider-dots span{width:5px;height:5px;border-radius:50%;background:#9aa4ad}
.slider-dots span.is-active{background:transparent;border:1px solid #cfd4d8}

/* Section headings */
.section-title{left:0;width:671px;text-align:center;font-family:"Ubuntu",sans-serif;font-size:16px}
.divider{left:289px;width:85px;height:10px}
.divider::before,.divider::after{content:"";position:absolute;top:4px;width:28px;height:1px;background:currentColor}
.divider::before{left:0}
.divider::after{right:0}
.divider i{position:absolute;left:37px;top:0;width:10px;height:10px;border-radius:50%;background:currentColor}

/* Offer cards */
.offer-card{top:498px;width:162px;height:157px;border-radius:2px;color:var(--white);text-align:center}
.offer-card.is-blue{background:var(--brand-blue)}
.offer-card.is-dark{background:var(--charcoal)}
.offer-icon{position:absolute;left:54px;top:-33px;width:54px;height:54px;border-radius:50%;border:2px solid var(--white);display:flex;align-items:center;justify-content:center}
.offer-icon.is-dark{background:var(--charcoal)}
.offer-icon.is-blue{background:var(--brand-blue)}
.offer-title{position:absolute;left:0;top:34px;width:100%;font-size:9.4px;font-weight:600}
.offer-text{position:absolute;left:10px;top:53px;width:142px;font-size:7.6px;line-height:11px}
.offer-text p+p{margin-top:11px}
.offer-button{position:absolute;left:51px;top:129px;width:61px;height:18px;font-size:7.6px;display:flex;align-items:center;justify-content:center;border-radius:2px;color:var(--white)}
.offer-button.is-dark{background:var(--charcoal)}
.offer-button.is-blue{background:var(--brand-blue)}

/* Services */
.services{left:0;top:679px;width:671px;height:303px;background:var(--charcoal)}
.service-card{top:768px;width:166px;height:182px;background:var(--white);padding:2px;text-align:center;color:var(--ink)}
.service-photo{width:162px;height:88px}
.service-title{margin-top:7px;font-family:"Ubuntu",sans-serif;font-size:9.8px}
.service-text{margin:5px auto 0;width:150px;font-size:7.2px;line-height:11px;height:33px}
.service-button{margin:6px auto 0;width:51px;height:15px;border:1px solid var(--ink);border-radius:3px;font-size:7.2px;display:flex;align-items:center;justify-content:center}

/* Contact */
.contact{left:0;top:982px;width:671px;height:186px;background:radial-gradient(ellipse at 50% 40%,#18324a 0%,#0d1d2c 55%,#070f17 100%)}
.contact-text{left:80px;top:1067px;width:511px;font-size:7.8px;line-height:14px;color:var(--muted);text-align:center}
.email-field{left:190px;top:1090px;width:209px;height:24px;background:var(--white);font-size:8px;color:#666;padding-left:9px;display:flex;align-items:center}
.submit-button{left:399px;top:1090px;width:83px;height:24px;background:var(--brand-blue-deep);color:var(--white);font-family:"Ubuntu",sans-serif;font-size:10px;display:flex;align-items:center;justify-content:center}
.social-links{left:283px;top:1134px;display:flex;gap:14px}
.social-links span{width:16px;height:16px;border-radius:50%;background:var(--white)}

/* Footer */
.site-footer{left:0;top:1168px;width:671px;height:32px;background:var(--brand-blue);color:var(--white);font-size:7.2px;display:flex;align-items:center;justify-content:center}
</style>
</head>
<body>

<div class="abs top-rule"></div>
<header class="abs site-header">
  <div class="abs brand">
    <span class="brand-mark"></span>
    <span class="brand-name">MERIDEL PROPERTY ACADEMY</span>
  </div>
  <nav class="abs main-nav">
    <a style="left:278px">HOME</a>
    <a style="left:327px">ABOUT US</a>
    <a style="left:391px">CAREERS</a>
    <a style="left:449px">SALARY</a>
    <a style="left:504px">DEGREES</a>
    <a style="left:563px">CONTACT US</a>
  </nav>
</header>

<section class="abs hero">
  <div class="abs hero-photo" role="img" aria-label="Man drawing a glowing line sketch of a house in the air, dark blue tones"></div>
  <svg class="abs hero-wave" viewBox="0 0 671 36" preserveAspectRatio="none"><path d="M0 0 Q335 26 671 0 V36 H0 Z" fill="#ffffff"/></svg>
  <h1 class="abs hero-title" style="top:126px">The Path to Your Future</h1>
  <div class="abs hero-button" style="top:174px">More Info</div>
  <div class="abs slider-dots" style="top:281px"><span class="is-active"></span><span></span><span></span><span></span></div>
</section>

<h2 class="abs section-title" style="top:409px">What We Offer</h2>
<div class="abs divider" style="top:433px;color:var(--brand-blue)"><i></i></div>

<article class="abs offer-card is-blue" style="left:55px">
  <div class="offer-icon is-dark">
    <svg width="24" height="24" viewBox="0 0 24 24" fill="none" stroke="#fff" stroke-width="2" stroke-linecap="round" stroke-linejoin="round"><path d="M12 3v16M6 13l6 6 6-6"/></svg>
  </div>
  <h3 class="offer-title">Get your license</h3>
  <div class="offer-text"><p>Dummy text is text that is used in the publishing industry or by web designlater be filled with 'real' content.</p><p>This is required when, for example, the final text is not yet available.</p></div>
  <div class="offer-button is-dark">Read More</div>
</article>

<article class="abs offer-card is-dark" style="left:254px">
  <div class="offer-icon is-blue">
    <svg width="24" height="24" viewBox="0 0 24 24"><rect x="8.5" y="4" width="7" height="4" rx="1" fill="none" stroke="#fff" stroke-width="1.8"/><rect x="3" y="7" width="18" height="13" rx="2" fill="#fff"/></svg>
  </div>
  <h3 class="offer-title">Post-Licensing</h3>
  <div class="offer-text"><p>Dummy text is text that is used in the publishing industry or by web designlater be filled with 'real' content.</p><p>This is required when, for example, the final text is not yet available.</p></div>
  <div class="offer-button is-blue">Read More</div>
</article>

<article class="abs offer-card is-blue" style="left:454px">
  <div class="offer-icon is-dark">
    <svg width="26" height="26" viewBox="0 0 24 24" fill="none" stroke="#fff" stroke-width="1.8" stroke-linecap="round"><circle cx="12" cy="12" r="9"/><path d="M12 7v5l3 2"/></svg>
  </div>
  <h3 class="offer-title">Continuing Education</h3>
  <div class="offer-text"><p>Dummy text is text that is used in the publishing industry or by web designlater be filled with 'real' content.</p><p>This is required when, for example, the final text is not yet available.</p></div>
  <div class="offer-button is-dark">Read More</div>
</article>

<section class="abs services"></section>
<h2 class="abs section-title" style="top:707px;color:var(--white)">Our Services</h2>
<div class="abs divider" style="top:732px;color:var(--white)"><i></i></div>

<article class="abs service-card" style="left:56px">
  <div class="service-photo" role="img" aria-label="Compass needle pointing to the word career" style="background:linear-gradient(135deg,#e9ddd6,#cdb8ad)"></div>
  <h3 class="service-title">Careers</h3>
  <p class="service-text">Career fields include residential and commercial real estate agents, brokers, mortgage brokers, property managers</p>
  <div class="service-button">Read More</div>
</article>

<article class="abs service-card" style="left:253px">
  <div class="service-photo" role="img" aria-label="Wooden letter blocks spelling salary on stacks of coins" style="background:linear-gradient(180deg,#8f98a3,#6b5a45)"></div>
  <h3 class="service-title">Salary</h3>
  <p class="service-text">According to the Norland Office of Trade Figures, real estate brokers earned a median annual wage of $56,860</p>
  <div class="service-button">Read More</div>
</article>

<article class="abs service-card" style="left:450px">
  <div class="service-photo" role="img" aria-label="Graduation cap and diploma on a stack of books" style="background:linear-gradient(135deg,#e7dfd4,#8a7563)"></div>
  <h3 class="service-title">Degrees</h3>
  <p class="service-text">A real estate license will provide all you will need to enter the real estate business. Each state has requirements</p>
  <div class="service-button">Read More</div>
</article>

<section class="abs contact" role="img" aria-label="Faint line drawing of a house on a dark navy background"></section>
<h2 class="abs section-title" style="top:998px;color:var(--white)">Contact Us</h2>
<div class="abs divider" style="top:1023px;color:var(--white)"><i></i></div>
<p class="abs contact-text" style="top:1049px">Maecenas aliquet velit vel turpis Mauris neque metus malesuada nec ultricies sit amet porttitor mattis enim In massa libero interdum nec interdum vel blandit sed nulla In ullamcorper est eget tempor cursus neque</p>
<div class="abs email-field">Email address</div>
<div class="abs submit-button">Submit</div>
<div class="abs social-links"><span></span><span></span><span></span><span></span></div>

<footer class="abs site-footer">©2016 Meridel Property Academy. All Right Reserved</footer>

</body>
</html>
```